Infografik für Tanzschule
Zielgruppe
Wir sind eine Tanzschule für die Tänze Salsa, Bachata, kizomba & Zouk in Freiburg
Aufgabenstellung
DESIGN-BRIEFING
Tarifübersicht – Tanzschule Ritmo del Alba
Projektziel
Gestaltung einer klaren, hochwertigen Tarifübersicht für eine Tanzschule.
Die Grafik dient: als Information & Orientierung auf der Homepage, als visuelle Grundlage für das Anmeldeformular vor Ort, Der Einstieg erfolgt immer über eine gratis Schnupperstunde.
Die verbindliche Anmeldung erfolgt nach der Schnupperstunde vor Ort über ein Formular mit Auswahlkästchen.
Grundaufbau
3 Tarifkarten nebeneinander
Einheitlicher, moderner Stil
evtl. Emotionale Bilder (echte Tanzszenen, echte Menschen)
Klare Hierarchie:
Titel → Preis → Erklärung → Vorteile → Auswahlkästchen
Struktur der Tarifkarten
KARTE 1 – EINSTIEG
Titel: 1× PRO WOCHE TANZEN
Preis: 56 €/ 39 € erm.
Subline: pro Person · pro Kalendermonat
Vorteile (max. 4 Bulletpoints):
Ein fester wöchentlicher Kurs
Klare Routine & Struktur
Ausweichstunde im selben Monat möglich (muss klar enthalten sein)
Auswahl: ☐ 1× pro Woche tanzen
KARTE 2 – REGELMÄSSIG TANZEN (darf visuell leicht hervorgehoben sein, z. B. Rahmen oder Badge)
Optionales Badge:
SEHR BELIEBT
Titel: 2× PRO WOCHE TANZEN
Preis: 98 € / 68 € erm.
Vorteile:
Zwei feste wöchentliche Kurse
Mehr Praxis & schnellerer Fortschritt
Ausweichstunde im selben Monat möglich
Auswahl:
☐ 2× pro Woche tanzen
KARTE 3 – MAXIMALE FREIHEIT
Titel: FLAT – ALL YOU CAN DANCE
Preis: ab 129 € / 99 € erm.
Alle Tänze
Alle Kurse (für dein Tanz-Level)
Alle Workshops (für dein Tanz-Level)
Maximale Freiheit
☐ FLAT 1 Monat – 149 € | 119 € erm. (monatlich kündbar)
☐ FLAT 3 Monate – 129 € | 99 € erm. (3 Monate Erstlaufzeit)
Einheitlicher Hinweis unter den Karten (kleiner Text)
Ausweic..

```html
<!DOCTYPE html>
<html lang="de">
<head>
<meta charset="utf-8">
<title>Anmeldeformular – Ritmo del Alba</title>
<link href="https://fonts.googleapis.com/css2?family=Inter:ital,wght@0,300;0,400;0,600;0,700;1,400&family=Barlow+Condensed:wght@400;500;600&display=swap" rel="stylesheet">
<style>
:root{
  --backdrop:#9d9d9d;
  --paper:#ffffff;
  --ink:#2a2a2a;
  --muted:#555;
  --rule:#8a8a8a;
  --card-bg:#f3f3f3;
  --card-border:#d9d9d9;
  --head-grey:#6e6e6e;
  --head-dark:#2a2a2a;
  --sepa-band:#dce4de;
  --photo-a:#6f7d62;
  --photo-b:#b9b2a4;
}
*{box-sizing:border-box;margin:0;padding:0}
html,body{width:1200px;height:1200px;overflow:hidden;background:var(--backdrop)}
body{font-family:"Inter",sans-serif;color:var(--ink)}
.sheet{position:absolute;left:302px;top:179px;width:595px;height:841px;background:var(--paper);overflow:hidden}
.abs{position:absolute}
.hero{left:0;top:0;width:595px;height:123px;background:linear-gradient(180deg,#8d98a0 0%,var(--photo-b) 35%,var(--photo-a) 100%)}
.hero-title{left:31px;top:15px;font-size:17px;font-weight:700;color:#fff;letter-spacing:-.3px}
.brand{right:40px;top:91px;color:#fff;font-size:10px;font-weight:400;display:flex;align-items:center;gap:5px}
.brand i{width:7px;height:7px;border-radius:50%;background:#fff;display:block}
.lbl{font-size:9.3px;color:var(--muted)}
.gender{left:36px;top:141px;font-size:8px;color:var(--muted);display:flex;gap:3px;align-items:center}
.box{display:inline-block;width:7px;height:7px;border:1px solid #444;border-radius:1.5px;vertical-align:middle;flex:none}
.row{left:36px;width:373px;height:14px}
.row .lbl{position:absolute;left:0;top:0}
.row .colon{position:absolute;left:96px;top:0;font-size:9.3px;color:var(--muted)}
.row .line{position:absolute;left:101px;right:0;top:12px;border-bottom:1px solid var(--rule)}
.opt{left:36px;font-size:9.3px;color:var(--muted);display:flex;gap:7px;align-items:center}
.contact{left:436px;top:145px;width:128px;height:145px;background:var(--card-bg);border:1px solid var(--card-border);border-radius:6px;padding:11px 5px;font-size:7.6px;line-height:11px;color:var(--muted);white-space:nowrap;letter-spacing:-.1px}
.contact b{color:var(--ink);font-weight:600}
.contact p{margin-bottom:12px}
.contact p:last-child{margin:0;line-height:13px}
.card{top:316px;width:170px;height:244px;background:var(--card-bg);border:1px solid var(--card-border);border-radius:8px;overflow:hidden}
.card-head{height:34px;padding:0 9px;display:flex;align-items:center;color:#fff;font-size:13.2px;font-weight:300;letter-spacing:-.5px;white-space:nowrap;background:var(--head-grey)}
.card.featured .card-head{background:var(--head-dark)}
.benefits{position:absolute;left:10px;right:10px;top:40px}
.benefits h4{font-size:9.5px;font-weight:600;letter-spacing:.3px;padding-bottom:3px;border-bottom:1.5px solid var(--ink)}
.benefits li{list-style:none;font-size:8.1px;letter-spacing:-.05px;color:var(--muted);padding:4px 0 3px;border-bottom:1px solid #dcdcdc;line-height:10px}
.benefits li.one{white-space:nowrap}
.choice{position:absolute;left:10px;font-size:8px;font-weight:600;display:flex;gap:6px;align-items:center;white-space:nowrap;letter-spacing:-.1px}
.choice-note{position:absolute;left:10px;font-size:7.6px;font-style:italic;color:var(--muted)}
.price{position:absolute;left:0;right:0;top:202px;text-align:center;font-size:9px;color:var(--muted)}
.price strong{font-size:19px;color:var(--ink);font-weight:600}
.price sup{font-size:8px;color:var(--ink);font-weight:600}
.price small{font-size:8px;color:var(--ink);font-weight:600;vertical-align:6px}
.price .per{display:block;margin-top:1px;font-size:8.5px}
.note h5{font-size:9.5px;font-weight:600;margin-bottom:4px}
.note div{border-left:2px solid #ccc;padding-left:8px;font-size:8.5px;font-style:italic;color:var(--muted);line-height:12.5px}
.band{left:0;top:655px;width:595px;height:186px;background:var(--sepa-band)}
.sepa{left:47px;top:667px;width:532px;height:102px;background:#fff;padding:5px 9px;font-family:"Barlow Condensed",sans-serif}
.sepa h6{font-size:8px;font-weight:600}
.sepa p{font-size:6.3px;line-height:9px;color:#444}
.bank{position:absolute;left:9px;top:46px;width:516px;height:49px;border:1px solid #222;font-family:"Barlow Condensed",sans-serif;font-size:7.4px}
.bank .r1{position:absolute;left:0;top:0;right:0;height:25px;border-bottom:1px solid #222}
.bank .split{position:absolute;left:295px;top:0;height:25px;border-left:1px solid #222}
.bank span{position:absolute}
.months{left:47px;top:783px;width:213px;height:24px;background:#fff;display:flex;justify-content:space-between;padding:3px 6px;font-family:"Barlow Condensed",sans-serif;font-size:6.5px;font-weight:500}
.months div{display:flex;flex-direction:column;align-items:center;gap:1px}
.cond{font-family:"Barlow Condensed",sans-serif;font-weight:500;font-size:12.5px;color:#333;white-space:nowrap}
.sign{left:330px;top:783px;width:249px;height:32px;background:#fff}
</style>
</head>
<body>
<main class="sheet">
  <div class="abs hero" role="img" aria-label="Gruppenfoto der Tanzlehrerinnen und Tanzlehrer vor der Stadtkulisse von Freiburg"></div>
  <h1 class="abs hero-title">Anmeldeformular</h1>
  <div class="abs brand"><i></i>Ritmo del Alba</div>

  <div class="abs gender">Frau <span class="box"></span> Herr <span class="box"></span> Div. <span class="box"></span></div>
  <div class="abs row" style="top:158px"><span class="lbl">Vorname / Nachname</span><span class="colon">:</span><span class="line"></span></div>
  <div class="abs row" style="top:178px"><span class="lbl">Straße / Nr</span><span class="colon">:</span><span class="line"></span></div>
  <div class="abs row" style="top:198px"><span class="lbl">PLZ/Ort</span><span class="colon">:</span><span class="line"></span></div>
  <div class="abs row" style="top:218px"><span class="lbl">Telefon</span><span class="colon">:</span><span class="line"></span></div>
  <div class="abs row" style="top:238px"><span class="lbl">E-mail</span><span class="colon">:</span><span class="line"></span></div>
  <div class="abs opt" style="top:258px"><span class="box"></span>Ermäßigt (Student*in / Schüler*in / Auszubildende*r)</div>
  <div class="abs opt" style="top:274px"><span class="box"></span>Ja, ich möchte den Newsletter und Kursinformationen erhalten.</div>

  <aside class="abs contact">
    <p><b>Tanzschule Ritmo del Alba</b><br>Lindenweg 14 79098 Freiburg</p>
    <p><b>Geschäftsanschrift</b><br>Ritmo del Alba Lena Hartmann<br>Uferstr. 8 79104 Freiburg</p>
    <p><b>T&nbsp;:</b> +49 151 000 123 45<br><b>M&nbsp;:</b> info@ritmo-del-alba.de<br><b>W&nbsp;:</b> www.ritmo-del-alba.de</p>
  </aside>

  <section class="abs card" style="left:31px">
    <div class="card-head">1× Pro Woche Tanzen</div>
    <div class="benefits"><h4>VORTEILE</h4><ul>
      <li class="one">Ein fester wöchentlicher Kurs</li><li class="one">Klare Routine &amp; Struktur</li><li>Ausweichstunde im selben Monat möglich</li></ul></div>
    <div class="choice" style="top:140px"><span class="box"></span>1× pro Woche tanzen</div>
    <div class="price"><strong>56</strong><sup>€</sup> / 38 € erm.<span class="per">pro Person / Kalendermonat</span></div>
  </section>

  <section class="abs card featured" style="left:213px">
    <div class="card-head">Regelmässig Tanzen</div>
    <div class="benefits"><h4>VORTEILE</h4><ul>
      <li class="one">Zwei feste wöchentliche Kurse</li><li class="one">Mehr Praxis &amp; schnellerer Fortschritt</li><li>Ausweichstunde im selben Monat möglich</li></ul></div>
    <div class="choice" style="top:140px"><span class="box"></span>2× pro Woche tanzen</div>
    <div class="price"><strong>98</strong><sup>€</sup> / 68 € erm.<span class="per">pro Person / Kalendermonat</span></div>
  </section>

  <section class="abs card" style="left:393px">
    <div class="card-head">Flat – All You Can Dance</div>
    <div class="benefits"><h4>VORTEILE</h4><ul>
      <li class="one">Alle Tänze</li><li class="one">Alle Kurse (für dein Tanz-Level)</li><li class="one">Alle Workshops (für dein Tanz-Level)</li><li class="one" style="border:0">Maximale Freiheit</li></ul></div>
    <div class="choice" style="top:140px"><span class="box"></span>FLAT 1 Monat – 149 € | 119 € erm.</div>
    <div class="choice-note" style="top:153px">(monatlich kündbar)</div>
    <div class="choice" style="top:167px"><span class="box"></span>FLAT 3 Monate – 129 € | 99 € erm.</div>
    <div class="choice-note" style="top:180px">(3 Monate Erstlaufzeit)</div>
    <div class="price"><small>ab</small><strong>129</strong><sup>€</sup> / 99 € erm.<span class="per">pro Person / Kalendermonat</span></div>
  </section>

  <div class="abs note" style="left:47px;top:595px;width:140px"><h5>Hinweis</h5><div>Ausweichstunde: Im selben Kalendermonat möglich.</div></div>
  <div class="abs note" style="left:226px;top:595px;width:350px"><h5>Verlängerung &amp; Kündigung</h5><div>Der Vertrag verlängert sich automatisch um jeweils einen Monat und ist mit 14 Tagen Frist zum Monatsende kündbar.<br>Ausnahme: FLAT 3 Monate – kündbar nach Ablauf der Erstlaufzeit.</div></div>

  <div class="abs band"></div>
  <section class="abs sepa">
    <h6>Einzugsermächtigung / SEPA-Lastschriftmandat</h6>
    <p>Ich ermächtige Ritmo del Alba, Zahlungen von meinem Konto per Lastschrift einzuziehen und mein Kreditinstitut, diese Lastschriften einzulösen. Bei Ablehnung der Lastschrift fallen Kosten von 10,00 € pro Rückbuchung an. Ich kann innerhalb von acht Wochen ab Belastungsdatum die Erstattung verlangen, gemäß den Bedingungen meines Kreditinstituts. Die Kursgebühr wird im ersten Monat zur Mitte/Ende eingezogen, danach jeweils am 05. jedes Monats.</p>
    <div class="bank">
      <div class="r1"></div><div class="split"></div>
      <span style="left:5px;top:3px">Kreditinstitut:</span>
      <span style="left:300px;top:3px">BIC: - Beginnt die IBAN mit DE, dann ist kein BIC nötig</span>
      <span style="left:5px;top:28px">IBAN:</span>
      <svg class="abs" style="left:0;top:25px" width="516" height="24" aria-hidden="true">
        <g stroke="#222" stroke-width="1">
          <line x1="27" y1="12" x2="27" y2="22"/><line x1="48" y1="12" x2="48" y2="22"/><line x1="69" y1="12" x2="69" y2="22"/>
          <line x1="89" y1="12" x2="89" y2="22"/><line x1="110" y1="5" x2="110" y2="22"/><line x1="131" y1="12" x2="131" y2="22"/>
          <line x1="151" y1="12" x2="151" y2="22"/><line x1="172" y1="12" x2="172" y2="22"/><line x1="193" y1="5" x2="193" y2="22"/>
          <line x1="213" y1="12" x2="213" y2="22"/><line x1="234" y1="12" x2="234" y2="22"/><line x1="255" y1="12" x2="255" y2="22"/>
          <line x1="275" y1="5" x2="275" y2="22"/><line x1="296" y1="12" x2="296" y2="22"/><line x1="317" y1="12" x2="317" y2="22"/>
          <line x1="337" y1="12" x2="337" y2="22"/><line x1="358" y1="5" x2="358" y2="22"/><line x1="379" y1="12" x2="379" y2="22"/>
          <line x1="399" y1="12" x2="399" y2="22"/><line x1="420" y1="12" x2="420" y2="22"/><line x1="441" y1="5" x2="441" y2="22"/>
          <line x1="461" y1="12" x2="461" y2="22"/><line x1="482" y1="12" x2="482" y2="22"/>
        </g>
        <text x="33" y="21" font-family="Barlow Condensed, sans-serif" font-size="13" font-weight="500">D</text>
        <text x="54" y="21" font-family="Barlow Condensed, sans-serif" font-size="13" font-weight="500">E</text>
      </svg>
    </div>
  </section>

  <div class="abs months">
    <div>Jan<span class="box"></span></div><div>Feb<span class="box"></span></div><div>Mrz<span class="box"></span></div>
    <div>Apr<span class="box"></span></div><div>Mai<span class="box"></span></div><div>Jun<span class="box"></span></div>
    <div>Jul<span class="box"></span></div><div>Aug<span class="box"></span></div><div>Sep<span class="box"></span></div>
    <div>Okt<span class="box"></span></div><div>Nov<span class="box"></span></div><div>Dez<span class="box"></span></div>
  </div>
  <div class="abs cond" style="left:48px;top:811px">Kursstart / Anmeldung ab:</div>
  <div class="abs sign"></div>
  <div class="abs cond" style="left:330px;top:818px">Datum / Unterschrift: <span style="font-size:6.5px;font-weight:600">Wir verweisen auf unsere umseitig abgedruckten AGB</span></div>
</main>
</body>
</html>
```